Business card for wedding & event planning company

I'm looking for a well designed double sided business card to represent my wedding and event planning company.

It should include the fact we manage the following events:
Weddings, birthdays, conferences, product launches, fashion shows & conventions
in the following areas:
Wiltshire, Oxfordshire, Berkshire & London

My contact details to be included are:

Moira Pennock
07715 482036
moira@amberlarkcelebrations.co.uk
www.amberlarkcelebrations.co.uk

My logo can be found at the following Filevaultex location:
AI file: https://www.filevaultex.com/s/k4mprt8wn31b7hz/brandlogo_sourcefile.ai?dl=0
PNG file:
https://www.filevaultex.com/s/h9qsle2vbx07mnd/brandlogo_image.png?dl=0

Target Market(s)

women aged 30-55

Industry/Entity Type

Wedding

Contact Information for Business Card

in the following areas:

Moira Pennock
Event Planner
07715 482036

Font styles to use
Serif
Sans Serif
Script

Requirements
Must have
• Purple and white colour scheme
Should not have
• Black background
• Please don't submit any of the see-through business card designs.

```html
<!DOCTYPE html>
<html lang="en">
<head>
<meta charset="utf-8">
<title>Amber Lark Celebrations – Business Card</title>
<link rel="stylesheet" href="https://fonts.googleapis.com/css2?family=Open+Sans:wght@400;600&display=swap">
<style>
  :root {
    --purple: #7f2b8e;
    --purple-dark: #6a2178;
    --purple-soft: #c9a6d1;
    --white: #ffffff;
    --paper: #f7f5f8;
    --backdrop: #e9e7ea;
    --rule: #b995c2;
  }
  * { box-sizing: border-box; margin: 0; padding: 0; }
  html, body {
    width: 1200px; height: 1000px; overflow: hidden;
    background: var(--backdrop);
    font-family: "Open Sans", Arial, sans-serif;
  }
  .card {
    position: absolute; left: 300px;
    width: 600px; height: 360px;
    border-radius: 22px; overflow: hidden;
    box-shadow: 0 6px 18px rgba(60, 20, 70, 0.18);
  }
  /* Front */
  .card-front { top: 90px; background: var(--purple); color: var(--white); }
  .brand {
    position: absolute; left: 0; right: 0; top: 70px;
    display: flex; flex-direction: column; align-items: center;
  }
  .brand-mark {
    width: 64px; height: 64px; border-radius: 50%;
    border: 2px solid var(--white); margin-bottom: 14px;
  }
  .brand-name {
    font-size: 40px; font-weight: 400; letter-spacing: 1px; line-height: 1.1;
  }
  .brand-sub {
    font-size: 15px; font-weight: 400; letter-spacing: 5px; text-transform: uppercase;
    margin-top: 4px; padding-bottom: 10px;
    border-bottom: 1px solid var(--rule); width: 300px; text-align: center;
  }
  .areas {
    position: absolute; left: 30px; right: 30px; bottom: 28px;
    display: flex; justify-content: space-between; list-style: none;
    font-size: 17px; font-weight: 600;
  }
  .areas li::before {
    content: ""; display: inline-block; width: 9px; height: 9px;
    background: var(--white); border-radius: 50%; margin-right: 7px;
    vertical-align: middle; position: relative; top: -2px;
  }
  /* Back */
  .card-back { top: 550px; background: linear-gradient(135deg, var(--white), var(--paper)); }
  .back-brand {
    position: absolute; left: 28px; top: 110px; width: 150px;
    display: flex; flex-direction: column; align-items: center; color: var(--purple-soft);
  }
  .back-brand .brand-mark { border-color: var(--purple-soft); width: 54px; height: 54px; }
  .back-brand .brand-name { font-size: 22px; text-align: center; }
  .contact {
    position: absolute; left: 200px; right: 28px; top: 48px;
    color: var(--purple);
  }
  .contact-name { font-size: 24px; font-weight: 600; margin-bottom: 22px; }
  .contact-list { list-style: none; }
  .contact-list li {
    display: flex; align-items: center; gap: 12px;
    font-size: 17px; font-weight: 600; margin-bottom: 14px;
    white-space: nowrap;
  }
  .contact-list li.phone { font-size: 21px; letter-spacing: 1px; }
  .icon { width: 28px; height: 28px; flex: none; }
  .services {
    position: absolute; left: 0; right: 0; bottom: 0; height: 88px;
    background: var(--purple); color: var(--purple-soft);
    display: flex; align-items: center; justify-content: center; text-align: center;
    font-size: 17px; line-height: 1.35; padding: 0 40px;
  }
</style>
</head>
<body>
  <section class="card card-front">
    <div class="brand">
      <span class="brand-mark"></span>
      <span class="brand-name">Amber Lark</span>
      <span class="brand-sub">Celebrations</span>
    </div>
    <ul class="areas">
      <li>Wiltshire</li>
      <li>Oxfordshire</li>
      <li>Berkshire</li>
      <li>London</li>
    </ul>
  </section>

  <section class="card card-back">
    <div class="back-brand">
      <span class="brand-mark"></span>
      <span class="brand-name">Amber Lark</span>
    </div>
    <div class="contact">
      <p class="contact-name">Moira Pennock</p>
      <ul class="contact-list">
        <li class="phone">
          <svg class="icon" viewBox="0 0 28 28" aria-hidden="true">
            <polygon points="14,1 26,8 26,20 14,27 2,20 2,8" fill="var(--purple)"/>
            <path d="M10 8 l3 3 -1.5 2 q1.5 3 4 4 l2-1.5 3 3 -2 2 q-6 0-10.5-10.5z" fill="var(--white)"/>
          </svg>
          07715 482036
        </li>
        <li>
          <svg class="icon" viewBox="0 0 28 28" aria-hidden="true">
            <polygon points="14,1 26,8 26,20 14,27 2,20 2,8" fill="var(--purple)"/>
            <rect x="8" y="10" width="12" height="8" fill="none" stroke="var(--white)" stroke-width="1.5"/>
            <path d="M8 10 l6 5 6-5" fill="none" stroke="var(--white)" stroke-width="1.5"/>
          </svg>
          moira@amberlarkcelebrations.co.uk
        </li>
        <li>
          <svg class="icon" viewBox="0 0 28 28" aria-hidden="true">
            <polygon points="14,1 26,8 26,20 14,27 2,20 2,8" fill="var(--purple)"/>
            <rect x="8" y="8.5" width="12" height="8.5" fill="none" stroke="var(--white)" stroke-width="1.5"/>
            <path d="M11 20 h6 M14 17 v3" stroke="var(--white)" stroke-width="1.5"/>
          </svg>
          www.amberlarkcelebrations.co.uk
        </li>
      </ul>
    </div>
    <p class="services">Weddings, Birthdays, Conferences, Product launches,<br>Fashion shows &amp; Conventions</p>
  </section>
</body>
</html>
```